Music video company site re-design :-)

Hi guys,

I run a small music video production company called "Copperlane Clip Studio".

It's the new year and I'm hoping to update our website design, but am at a bit of a loss - which is where I'm desperately hoping you can help!

I need something cool and contemporary but not utterly terrifying/confusing that your average band manager/solo artist funding their own music video for the first time, won't be put off.

If you can check out our current website (http://www.CopperlaneClipStudio.example) I think that would probably help :-)

Target Market(s)

Solo music artists and managers of small groups/bands.

Industry/Entity Type

It Company

Requirements
Must have
• Clear, cool but accessible.

I'll need to be able to embed Vimeo videos from our Vimeo-plus account into the pages...

http://www.streamvault.example/copperlaneclips

I'd also like to be able to optimise the site for search engines, so we'll need text and not images with text in them.

I'd also like to include or use images from our videos throughout the site, so if you can include as many of these as possible that would be great.

I've uploaded a zip file with them in, how they are used is up to you guys, but the more the merrier.
Should not have
• Images of cameras, lights, clapper boards etc...

No bloody Times New Roman unless you are really reinventing that wheel or trying to make it look like my nan made my website with clip art.

Also, no god damn emoticons ;-)

```html
<!DOCTYPE html>
<html lang="en">
<head>
<meta charset="utf-8">
<title>Copperlane Clip Studio</title>
<link href="https://fonts.googleapis.com/css2?family=Kaushan+Script&family=Open+Sans:wght@400;700;800&display=swap" rel="stylesheet">
<style>
:root{
  --red:#f0244a;
  --red-deep:#a50f2a;
  --ink:#000;
  --white:#fff;
  --grey:#8a8a8a;
  --panel:#111;
  --field-border:#5a1020;
}
*{box-sizing:border-box;margin:0;padding:0}
html,body{width:1200px;height:1172px;overflow:hidden;background:var(--ink)}
body{position:relative;font-family:"Open Sans",Verdana,sans-serif;color:var(--white)}
.abs{position:absolute}
.header-band{left:0;top:0;width:1200px;height:600px;
  background:linear-gradient(180deg,#0a0a0a 0%,#0d0d0d 70%,#3a3a3a 92%,#000 100%)}
.splash-art{left:0;top:0;width:360px;height:560px;
  background:radial-gradient(ellipse at 30% 12%,#b3101f 0%,#5a0810 30%,transparent 55%),
  radial-gradient(ellipse at 30% 78%,#e8e8e8 0%,#9a9a9a 30%,transparent 60%)}
.splash-right{left:1110px;top:0;width:90px;height:560px;
  background:radial-gradient(ellipse at 80% 20%,#3a3a3a 0%,transparent 70%)}
.phone{left:884px;top:20px;display:flex;align-items:center;gap:10px;
  font-family:"Kaushan Script",cursive;font-size:29px;color:var(--red);line-height:1}
.logo{left:0;width:1384px;top:86px;text-align:center;font-weight:800;
  font-size:42px;color:var(--red);letter-spacing:-1px}
.main-nav a{position:absolute;top:174px;font-family:"Kaushan Script",cursive;
  font-size:24px;color:var(--white);text-decoration:none;white-space:nowrap}
.main-nav a.current{color:var(--red)}
.reel-frame{left:356px;top:221px;width:741px;height:384px;border:2px solid var(--red);border-radius:8px}
.reel-main{left:365px;top:230px;width:521px;height:365px;
  background:radial-gradient(ellipse at 45% 55%,#7a5a48 0%,#3a2a24 40%,#0c0a0a 80%)}
.reel-title{left:376px;top:240px;font-weight:800;font-size:33px;color:#c8c8c8;letter-spacing:-1px}
.thumb{left:893px;width:194px;height:114px}
.thumb-1{top:232px;background:linear-gradient(120deg,#7a1a20,#c9a8a0 60%,#5a3a30)}
.thumb-2{top:356px;background:linear-gradient(90deg,#d8d8d8,#a0a0a0 50%,#e8e8e8)}
.thumb-3{top:480px;background:linear-gradient(120deg,#2a4a6a,#b89070 55%,#1a1a1a)}
.play{position:absolute}
.scrollbar{left:1102px;top:221px;width:26px;height:384px;border:2px solid var(--red);border-radius:8px}
.scrollbar .track{position:absolute;left:10px;top:10px;width:3px;height:360px;background:var(--red)}
.scrollbar .knob{position:absolute;left:4px;top:32px;width:15px;height:15px;border-radius:50%;background:var(--white);border:2px solid var(--red)}
.col-title{font-family:"Kaushan Script",cursive;font-size:23px;color:var(--red);top:645px;white-space:nowrap}
.copy{font-size:15.6px;line-height:20.4px;text-align:justify}
.copy p+p{margin-top:20.4px}
.divider{top:684px;width:2px;height:360px;background:linear-gradient(180deg,transparent,var(--red-deep) 20%,var(--red) 50%,var(--red-deep) 80%,transparent)}
.read-more{width:91px;height:29px;background:linear-gradient(180deg,#fff,#d8d8d8);
  color:#6a0a14;font-size:10px;font-weight:800;letter-spacing:1px;display:flex;align-items:center;justify-content:center}
.promo-video{left:499px;top:703px;width:304px;height:191px;border:1px solid #333;
  background:linear-gradient(90deg,#0a0614 0%,#5a2a9a 25%,#1a0a2a 45%,#6a3aa8 70%,#0a0614 100%)}
.promo-still{left:620px;top:706px;width:70px;height:158px;
  background:linear-gradient(180deg,#c0603a,#d82030 60%,#901820)}
.player-bar{left:499px;top:866px;width:304px;height:28px;background:linear-gradient(180deg,#d8d8d8,#8a8a8a);border-radius:0 0 4px 4px}
.field{left:886px;width:276px;border:1px solid #6a6a6a;background:#000;color:var(--red);font-size:15.6px;padding:3px 6px}
.btn{top:1015px;height:32px;display:flex;align-items:center;justify-content:center;font-size:17px;
  background:linear-gradient(180deg,#f0405a,#b0102a);color:var(--white)}
.footer-rule{left:0;top:1100px;width:1200px;height:1px;background:#2a2a2a}
.footer-nav{left:0;top:1117px;width:1200px;text-align:center;font-size:15.6px}
.footer-nav .current{color:var(--red)}
.legal{left:0;top:1141px;width:1200px;text-align:center;font-size:11px;color:var(--red)}
</style>
</head>
<body>
<div class="abs header-band"></div>
<div class="abs splash-art" role="img" aria-label="Red ink splatter with white silhouettes of a band performing on a paint swoosh"></div>
<div class="abs splash-right" role="img" aria-label="Grey ink splatter"></div>

<div class="abs phone">
  <svg width="36" height="28" viewBox="0 0 36 28" aria-hidden="true">
    <path d="M3 9 Q18 -2 33 9 L30 13 L24 11 L24 8 Q18 6 12 8 L12 11 L6 13 Z" fill="var(--red)"/>
    <rect x="7" y="14" width="22" height="13" rx="3" fill="var(--red)"/>
    <circle cx="18" cy="20" r="4" fill="#000"/>
  </svg>
  <span>07700 900 123</span>
</div>

<div class="abs logo">copperlaneclipstudio</div>

<nav class="main-nav">
  <a class="current" style="left:379px">Home</a>
  <a style="left:468px">Music Video</a>
  <a style="left:626px">Promo Future</a>
  <a style="left:799px">Band Site Design</a>
  <a style="left:1018px">Prices</a>
</nav>

<div class="abs reel-frame"></div>
<div class="abs reel-main" role="img" aria-label="Showreel still of a tattooed dancer in silver jewellery"></div>
<div class="abs reel-title">Showreel 2010</div>
<svg class="play" style="left:592px;top:378px" width="66" height="66" viewBox="0 0 66 66" aria-hidden="true">
  <circle cx="33" cy="33" r="30" fill="rgba(0,0,0,.45)" stroke="var(--red)" stroke-width="3"/>
  <path d="M24 18 L48 33 L24 48 L30 33 Z" fill="#ddd"/>
</svg>

<div class="abs thumb thumb-1" role="img" aria-label="Video still of an artist in a fur coat"></div>
<div class="abs thumb thumb-2" role="img" aria-label="Video still of two performers in a white room"></div>
<div class="abs thumb thumb-3" role="img" aria-label="Video still of a singer with a microphone"></div>
<svg class="play" style="left:976px;top:270px" width="40" height="40" viewBox="0 0 40 40" aria-hidden="true"><circle cx="20" cy="20" r="18" fill="rgba(0,0,0,.55)" stroke="var(--red)" stroke-width="2"/><path d="M15 11 L29 20 L15 29 L18 20 Z" fill="#ddd"/></svg>
<svg class="play" style="left:976px;top:394px" width="40" height="40" viewBox="0 0 40 40" aria-hidden="true"><circle cx="20" cy="20" r="18" fill="rgba(0,0,0,.55)" stroke="var(--red)" stroke-width="2"/><path d="M15 11 L29 20 L15 29 L18 20 Z" fill="#ddd"/></svg>
<svg class="play" style="left:976px;top:518px" width="40" height="40" viewBox="0 0 40 40" aria-hidden="true"><circle cx="20" cy="20" r="18" fill="rgba(0,0,0,.55)" stroke="var(--red)" stroke-width="2"/><path d="M15 11 L29 20 L15 29 L18 20 Z" fill="#ddd"/></svg>

<div class="abs scrollbar"><span class="track"></span><span class="knob"></span></div>

<h2 class="abs col-title" style="left:34px">Welcome to CopperlaneClipStudio.example</h2>
<div class="abs copy" style="left:36px;top:700px;width:401px">
  <p>“ I have a great working relationship with CCS and remain continually impressed with their professionalism throughout any of my projects. ”</p>
  <p>We're a London based music video production company that specialise in affordable band promo and music video production - whether it's for unsigned artists, specialist performers or large record labels - no matter what the genre or style of your music/performance, we can help you promote it!</p>
  <p>Our music videos have been broadcast on Vibe TV, Vibe Base, Vibe Europe,The Crate, Channel Q, The Chart Channel, Homeview Urban Mix, to name a few.</p>
</div>
<div class="abs read-more" style="left:346px;top:1022px">READ MORE</div>

<div class="abs divider" style="left:463px"></div>

<h2 class="abs col-title" style="left:493px">Promo Package</h2>
<div class="abs promo-video" role="img" aria-label="Promo video still with violet light bars"></div>
<div class="abs promo-still" role="img" aria-label="Dancer in a red top"></div>
<div class="abs player-bar">
  <svg width="304" height="28" viewBox="0 0 304 28" aria-hidden="true">
    <path d="M12 8 L21 14 L12 20 Z" fill="#555"/>
    <rect x="36" y="9" width="3" height="10" fill="#555"/><rect x="42" y="9" width="3" height="10" fill="#555"/>
    <rect x="64" y="10" width="8" height="8" fill="#555"/>
    <rect x="84" y="7" width="106" height="14" fill="#f4f4f4" stroke="#666"/>
    <path d="M210 11 h4 l5 -4 v14 l-5 -4 h-4 Z" fill="#333"/>
    <path d="M228 20 L288 20 L288 8 Z" fill="#f4f4f4" stroke="#666"/>
  </svg>
</div>
<div class="abs copy" style="left:484px;top:904px;width:327px">
  <p>Great music isn't enough. People need to hear it, but sometimes they need to see it. Seeing a performance will help fans connect with a performer or group in ways that the music alone never could.</p>
</div>
<div class="abs read-more" style="left:720px;top:1018px">READ MORE</div>

<div class="abs divider" style="left:846px"></div>

<h2 class="abs col-title" style="left:884px">Contact Us</h2>
<div class="abs copy" style="left:884px;top:698px;width:276px">
  <p>Advice or to chat about what you have in mind for your next music video. For more information Please Fill the form or</p>
  <p style="margin:0;text-align:right">call 07700 900 123</p>
</div>
<form>
  <div class="abs field" style="top:810px;height:28px">Name:</div>
  <div class="abs field" style="top:846px;height:28px">Phone No:</div>
  <div class="abs field" style="top:882px;height:28px">E-mail:</div>
  <div class="abs field" style="top:918px;height:84px">Comments:</div>
  <div class="abs btn" style="left:888px;width:134px">Reset</div>
  <div class="abs btn" style="left:1025px;width:136px">Submit</div>
</form>

<div class="abs footer-rule"></div>
<nav class="abs footer-nav"><span class="current">Home</span> | Music Video | Promo Future | Band Site Design | Prices | Contact Us | Sitemap</nav>
<div class="abs legal">Copyright © 2003-2011 Copperlaneclipstudio.example. All rights reserved. / Terms of Service / Privacy Statement</div>
</body>
</html>
```